Bref créative
The Marlowe Gala
Event Planning
Professional
Rosalind Hartwell
Owner - The Marlowe Gala
4105 - 27 Ashcombe Avenue
Toronto, ON M5R 2K7
rosalind@TheMarloweGala.example
www.TheMarloweGala.example
The card can be single or double sided i don't mind. Just be creative and make it clean!!!
Thanks!
It can be single or double sided I dont mind.

```html
<!DOCTYPE html>
<html lang="en">
<head>
<meta charset="utf-8">
<title>The Marlowe Gala — Business Cards</title>
<link rel="stylesheet" href="https://fonts.googleapis.com/css2?family=Montserrat:wght@400;600&display=swap">
<style>
  :root {
    --backdrop: #d8d5d2;
    --card-top-light: #ffffff;
    --card-top-mid: #e4e4e4;
    --band-mid: #7d7e80;
    --band-dark: #5f6062;
    --silver-hi: #f4f4f4;
    --silver-lo: #9a9a9a;
    --ink: #6c6d70;
    --ink-light: #f2f2f2;
  }
  * { box-sizing: border-box; margin: 0; padding: 0; }
  html, body { width: 1200px; height: 742px; overflow: hidden; }
  body {
    background: var(--backdrop);
    font-family: "Montserrat", sans-serif;
    position: relative;
  }
  .card {
    position: absolute;
    width: 440px;
    height: 262px;
    border-radius: 18px;
    overflow: hidden;
    display: flex;
    flex-direction: column;
    box-shadow: 0 6px 16px rgba(0,0,0,.18);
  }
  .card--front.card--left  { left: 140px; top: 92px; }
  .card--front.card--right { left: 620px; top: 92px; }
  .card--back.card--left   { left: 140px; top: 392px; }
  .card--back.card--right  { left: 620px; top: 392px; }

  .card-top {
    flex: 0 0 150px;
    background: linear-gradient(180deg, var(--card-top-light) 0%, var(--card-top-mid) 100%);
    display: flex;
    flex-direction: column;
    align-items: center;
    justify-content: center;
    gap: 8px;
  }
  .card--back .card-top { flex-basis: 132px; }

  .brand-mark {
    width: 46px; height: 46px;
    background: var(--ink);
  }
  .brand-name {
    font-size: 15px;
    font-weight: 400;
    letter-spacing: 2px;
    text-transform: uppercase;
    color: var(--ink);
  }
  .brand-tag {
    font-size: 9px;
    letter-spacing: 3px;
    color: var(--ink);
    margin-top: -6px;
  }

  .silver-rule {
    flex: 0 0 6px;
    background: linear-gradient(90deg, var(--silver-lo) 0%, var(--silver-hi) 45%, var(--silver-lo) 70%, var(--silver-hi) 100%);
  }

  .name-bar {
    flex: 0 0 26px;
    background: linear-gradient(180deg, #d8d8d8, #bdbdbd);
    display: flex;
    align-items: center;
    justify-content: center;
    gap: 8px;
    font-size: 9px;
    color: #4a4b4d;
  }
  .name-bar .person { font-weight: 600; }

  .contact {
    flex: 1;
    background: linear-gradient(180deg, var(--band-mid), var(--band-dark));
    padding: 16px 22px 0;
    color: var(--ink-light);
    font-size: 8.5px;
    display: flex;
    flex-direction: column;
    gap: 10px;
  }
  .contact-row { display: flex; gap: 18px; align-items: center; }
  .contact-item { display: flex; align-items: center; gap: 5px; white-space: nowrap; }
  .contact-item svg { width: 11px; height: 11px; flex: none; }

  .back-band {
    flex: 1;
    background: linear-gradient(180deg, var(--band-mid), var(--band-dark));
    display: flex;
    align-items: flex-end;
    justify-content: center;
    padding-bottom: 28px;
  }
  .web {
    font-size: 9px;
    letter-spacing: 2.5px;
    color: var(--ink-light);
  }

  /* frosted translucent variant */
  .card--frost .card-top { background: linear-gradient(180deg, rgba(255,255,255,.75), rgba(225,222,220,.6)); }
  .card--frost .name-bar { background: rgba(205,205,205,.8); }
  .card--frost .contact,
  .card--frost .back-band { background: linear-gradient(180deg, rgba(125,126,128,.88), rgba(95,96,98,.88)); }
  .card--frost .brand-mark { background: #8a8b8d; }
  .card--frost .brand-name, .card--frost .brand-tag { color: #8a8b8d; }
</style>
</head>
<body>

<svg width="0" height="0" style="position:absolute">
  <defs>
    <symbol id="icon-pin" viewBox="0 0 12 12"><circle cx="6" cy="6" r="6" fill="#ffffff"/><path d="M6 2.6a2.2 2.2 0 0 0-2.2 2.2C3.8 6.6 6 9.4 6 9.4s2.2-2.8 2.2-4.6A2.2 2.2 0 0 0 6 2.6z" fill="#5f6062"/></symbol>
    <symbol id="icon-phone" viewBox="0 0 12 12"><circle cx="6" cy="6" r="6" fill="#ffffff"/><path d="M4 3.2l1 .2.5 1.5-.7.6a4 4 0 0 0 1.7 1.7l.6-.7 1.5.5.2 1-.8.8C5.6 8.6 3.4 6.4 3.2 4z" fill="#5f6062"/></symbol>
    <symbol id="icon-mobile" viewBox="0 0 12 12"><circle cx="6" cy="6" r="6" fill="#ffffff"/><rect x="4.3" y="2.8" width="3.4" height="6.4" rx=".6" fill="#5f6062"/></symbol>
    <symbol id="icon-mail" viewBox="0 0 12 12"><circle cx="6" cy="6" r="6" fill="#ffffff"/><rect x="3" y="4" width="6" height="4" fill="#5f6062"/><path d="M3 4l3 2.2L9 4" stroke="#fff" stroke-width=".6" fill="none"/></symbol>
  </defs>
</svg>

<!-- front, solid -->
<section class="card card--front card--left">
  <div class="card-top">
    <div class="brand-mark"></div>
    <div class="brand-name">The Marlowe Gala</div>
  </div>
  <div class="silver-rule"></div>
  <div class="name-bar"><span class="person">Rosalind Hartwell</span><span>|</span><span>Owner - The Marlowe Gala</span></div>
  <div class="contact">
    <div class="contact-row">
      <span class="contact-item"><svg><use href="#icon-pin"/></svg>4105 - 27 Ashcombe Avenue Toronto, ON M5R 2K7</span>
    </div>
    <div class="contact-row">
      <span class="contact-item"><svg><use href="#icon-phone"/></svg>416.555.0134</span>
      <span class="contact-item"><svg><use href="#icon-mobile"/></svg>416.555.0178</span>
      <span class="contact-item"><svg><use href="#icon-mail"/></svg>rosalind@TheMarloweGala.example</span>
    </div>
  </div>
</section>

<!-- front, frosted -->
<section class="card card--front card--right card--frost">
  <div class="card-top">
    <div class="brand-mark"></div>
    <div class="brand-name">The Marlowe Gala</div>
  </div>
  <div class="silver-rule"></div>
  <div class="name-bar"><span class="person">Rosalind Hartwell</span><span>|</span><span>Owner - The Marlowe Gala</span></div>
  <div class="contact">
    <div class="contact-row">
      <span class="contact-item"><svg><use href="#icon-pin"/></svg>4105 - 27 Ashcombe Avenue Toronto, ON M5R 2K7</span>
    </div>
    <div class="contact-row">
      <span class="contact-item"><svg><use href="#icon-phone"/></svg>416.555.0134</span>
      <span class="contact-item"><svg><use href="#icon-mobile"/></svg>416.555.0178</span>
      <span class="contact-item"><svg><use href="#icon-mail"/></svg>rosalind@TheMarloweGala.example</span>
    </div>
  </div>
</section>

<!-- back, solid -->
<section class="card card--back card--left">
  <div class="card-top">
    <div class="brand-mark"></div>
    <div class="brand-name">The Marlowe Gala</div>
    <div class="brand-tag">Event Planning</div>
  </div>
  <div class="silver-rule"></div>
  <div class="back-band"><span class="web">www.TheMarloweGala.example</span></div>
</section>

<!-- back, frosted -->
<section class="card card--back card--right card--frost">
  <div class="card-top">
    <div class="brand-mark"></div>
    <div class="brand-name">The Marlowe Gala</div>
    <div class="brand-tag">Event Planning</div>
  </div>
  <div class="silver-rule"></div>
  <div class="back-band"><span class="web">www.TheMarloweGala.example</span></div>
</section>

</body>
</html>
```